CBD Lotion package Design plus Box

Hi! We need a packaging design and a box for a CBD infused hand/ body lotion. Our company name is Orvessa and the product is called Marzelune. I think this will be our "flagship product" we are looking for a design that has a big Wow factor, it has to look modern, clean, and look like a premium brand. My 1st thought is a graffiti theme, but I'm open to any concept.

A. A few requirements-
1. No more then 2 colors (design)
2. The bottle & cap can be any color
3. No cannabis or hemp leaves please

B. Front of the bottle has to have the below items
Marzelune - Focus
Hemp Lotion
100% Natural
Orvessa logo - incorporated
250 MG CBD
7 oz
Fragrance: Jasmine Sambac

C. Back of the bottle has to have:

1.Attached QR code - Under the code can you please add or www.orvessa.com/lab-report

2. Bar code

----below is updated---4/4/19

Ingredients: Organic Aloe Leaf Juice, Organic Coconut Oil, Glycerin, Stearic Acid, Emulsifying Wax, Witch Hazel Water, Vitamin E, Sunflower Seed Oil, Phenoxyethanol, Organic Hemp Seed Oil, Rose Flower Water, Organic White Willow Bark Extract, Organic Rosemary Leaf Extract, Organic Neem Seed Oil, Organic Alcohol, Xanthan Gum, Tetrasodium Glutamate Diacetate

Directions: Apply to the hands & body as often as needed throughout the day to hydrate and nourish the skin.

Storage: Keep product in a cool dry play out of direct sunlight

84% Organic Content

Disclaimer: Consult your doctor before taking if you are pregnant or nursing, have a medical condition, or take pharmaceutical drugs. The statements made regarding these products have not been evaluated by the National Wellness Review Board. The efficacy of these products has not been confirmed by NWRB-approved research. These products are not intended to diagnose, treat, cure or prevent any disease. Warring- for external use only: do not get into eyes. Keep out of the reach of children.

5. Box same as the lotion back ( C) . The front (B) + logo or design concept from the bottle is fine

Target Market(s)

Millennials - Baby Boomers
Middle-Upper Income
Live in close Urben area (NYC, LA, ect)

Industry/Entity Type

Cosmetic

Colors

Designer to choose colors to be used in the design.

Requirements
Must have
• A. A few requirements-
• 1. No more then 2 colors (design)
• 2. The bottle & cap can be any color
• Front of the bottle has to have the below items
• Marzelune - main Focus
• Hemp Lotion -small
• 100% Natural - small
• Orvessa logo - 2nd emphasis
• 250 MG CBD
• 7 oz
• Fragrance: Jasmine Sambac
• ***Please see description
Nice to have
Should not have
• No cannabis or hemp leaves please

```html
<!DOCTYPE html>
<html lang="en">
<head>
<meta charset="utf-8">
<title>Orvessa — Marzelune Hemp Lotion</title>
<link rel="stylesheet" href="https://fonts.googleapis.com/css2?family=Leckerli+One&family=Playfair+Display:wght@700&family=Roboto+Condensed:wght@400&display=swap">
<style>
  :root {
    --backdrop: #6d6e70;
    --ink: #2e2a5e;
    --lilac: #dcd8f0;
    --lilac-soft: #e6e3f6;
  }
  html, body {
    margin: 0;
    padding: 0;
    width: 1200px;
    height: 1200px;
    overflow: hidden;
    background: var(--backdrop);
  }
  .stage {
    position: relative;
    width: 1200px;
    height: 1200px;
  }
  .label {
    position: absolute;
    top: 120px;
    width: 440px;
    height: 960px;
  }
  .label--dark { left: 140px; }
  .label--light { left: 620px; }
  .brand-name {
    font-family: "Playfair Display", serif;
    font-weight: 700;
    font-size: 24px;
  }
  .product-name {
    font-family: "Leckerli One", cursive;
    font-size: 80px;
  }
  .product-type {
    font-family: "Playfair Display", serif;
    font-weight: 700;
    font-size: 26px;
    letter-spacing: 0.5px;
  }
  .product-claim {
    font-family: "Playfair Display", serif;
    font-weight: 700;
    font-size: 17px;
  }
  .fragrance {
    font-family: "Roboto Condensed", sans-serif;
    font-size: 25px;
  }
  .net-weight {
    font-family: "Playfair Display", serif;
    font-weight: 700;
    font-size: 24px;
  }
</style>
</head>
<body>
<main class="stage">

  <!-- Dark-top label -->
  <svg class="label label--dark" viewBox="0 0 440 960" xmlns="http://www.w3.org/2000/svg">
    <rect width="440" height="960" fill="var(--lilac)"/>
    <polygon points="0,0 440,0 440,590 220,660 0,590" fill="var(--ink)"/>
    <polyline points="0,610 220,680 440,610" fill="none" stroke="var(--ink)" stroke-width="4"/>

    <circle cx="220" cy="120" r="9" fill="none" stroke="var(--lilac)" stroke-width="2"/>
    <text class="brand-name" x="220" y="198" text-anchor="middle" fill="var(--lilac)">Orvessa</text>

    <text class="product-name" x="220" y="425" text-anchor="middle" fill="var(--lilac)">Marzelune</text>

    <text class="product-type" x="220" y="748" text-anchor="middle" fill="var(--ink)">HEMP LOTION</text>
    <line x1="100" y1="766" x2="340" y2="766" stroke="var(--ink)" stroke-width="1.5"/>
    <text class="product-claim" x="220" y="792" text-anchor="middle" fill="var(--ink)">100% Natural</text>
    <line x1="100" y1="808" x2="340" y2="808" stroke="var(--ink)" stroke-width="1.5"/>

    <rect x="0" y="826" width="440" height="46" fill="var(--ink)"/>
    <text class="fragrance" x="220" y="858" text-anchor="middle" fill="var(--lilac-soft)">Jasmine Sambac</text>

    <text class="net-weight" x="220" y="930" text-anchor="middle" fill="var(--ink)">7 oz</text>
  </svg>

  <!-- Light-top label with chevron band -->
  <svg class="label label--light" viewBox="0 0 440 960" xmlns="http://www.w3.org/2000/svg">
    <rect width="440" height="960" fill="var(--lilac)"/>
    <polyline points="0,232 220,296 440,232" fill="none" stroke="var(--ink)" stroke-width="4"/>
    <polygon points="0,252 220,316 440,252 440,550 220,612 0,550" fill="var(--ink)"/>
    <polyline points="0,570 220,632 440,570" fill="none" stroke="var(--ink)" stroke-width="4"/>

    <circle cx="220" cy="120" r="9" fill="none" stroke="var(--ink)" stroke-width="2"/>
    <text class="brand-name" x="220" y="198" text-anchor="middle" fill="var(--ink)">Orvessa</text>

    <text class="product-name" x="220" y="455" text-anchor="middle" fill="var(--lilac)">Marzelune</text>

    <text class="product-type" x="220" y="748" text-anchor="middle" fill="var(--ink)">HEMP LOTION</text>
    <line x1="100" y1="766" x2="340" y2="766" stroke="var(--ink)" stroke-width="1.5"/>
    <text class="product-claim" x="220" y="792" text-anchor="middle" fill="var(--ink)">100% Natural</text>
    <line x1="100" y1="808" x2="340" y2="808" stroke="var(--ink)" stroke-width="1.5"/>

    <rect x="0" y="826" width="440" height="46" fill="var(--ink)"/>
    <text class="fragrance" x="220" y="858" text-anchor="middle" fill="var(--lilac-soft)">Jasmine Sambac</text>

    <text class="net-weight" x="220" y="930" text-anchor="middle" fill="var(--ink)">7 oz</text>
  </svg>

</main>
</body>
</html>
```